We need a package design for a dietary supplement.

We need a package design for a dietary supplement - throwable tablets - Senegalese acacia fiber with pineapple flavor.
New name BrioKern.
Remember the packaging is a white jar, a magenta cap, a sticker, and a cardboard box. We want to change the name to: BrioKern (if you have a better idea for the name, just tell me) and refresh the packaging.
Product description:
> Contributes to improving the functioning of the digestive system.
> Boosts metabolism, controls appetite and supports weight loss.
> Helps maintain normal blood sugar levels.
> Regulates cholesterol levels
> 100% natural ingredients in the form of chewable tablets.
It has many beneficial health benefits:
> Cleanses the body of toxins,
> Helps with constipation and bloating,
> Facilitates defecation,
> Regulates cholesterol levels (by eliminating bile acids from the intestine),
> Adds energy,
> Improves metabolism,
> reduces appetite,
> Improves the work of the digestive system,
> It can help to get rid of the unpleasant smell from the mouth,
> Improves well-being,
> Regular intake can lead to weight loss,
> It works gently and does not cause side effects,
> Delays the aging process,
> Improves the appearance of the skin
This all-natural dietary supplement supports heart health, helps maintain blood sugar levels, soothes irritable bowel syndrome, and improves overall gut health.

100% natural, vegan product, no added sugars, no added salt. It has only 2 ingredients: Cenegal acacia and pineapple juice.

We are changing the name and packaging for our product called DunaMarsk. Photos attached, packaging grid attached, samples of our other packaging attached.
*Packaging in Dutch

Target Market(s)

Netherlands

Industry/Entity Type

dietary supplements

Colors

Designer to choose colors to be used in the design.

Requirements
Must have
• Modern and inspire patient confidence.
Nice to have
• Good, natural, healthy
Should not have
• It should not clearly indicate that it has a slimming effect, as in the dunamarsk project

```html
<!DOCTYPE html>
<html lang="en">
<head>
<meta charset="utf-8">
<title>BrioKern – Senegalese Acacia Fiber label</title>
<link rel="stylesheet" href="https://fonts.googleapis.com/css2?family=Bebas+Neue&family=Montserrat:wght@400;700;800&family=Oswald:wght@300;400&display=swap">
<style>
  :root {
    --canvas: #ffffff;
    --label-top: #f4f4f4;
    --label-mid: #e9e9e9;
    --ink: #0a0a0a;
    --brand-grey: #6d6d6d;
    --brand-dark: #3a3a3a;
    --leaf-dark: #1f3a12;
    --leaf: #4e6b36;
    --band-black: #000000;
    --band-orange: #b4541f;
    --band-orange-light: #c8632a;
    --band-green: #3b5225;
    --band-green-light: #566f3c;
    --rule-green: #4b6b2f;
    --white: #ffffff;
    --fruit-yellow: #f2c21a;
    --gum-amber: #a4502a;
  }
  html, body {
    margin: 0;
    padding: 0;
    width: 1200px;
    height: 1200px;
    overflow: hidden;
    background: var(--canvas);
  }
  .label {
    position: absolute;
    left: 120px;
    top: 65px;
    width: 960px;
    height: 1070px;
    overflow: hidden;
    background: linear-gradient(180deg, var(--label-top) 0%, var(--label-mid) 55%, var(--label-top) 100%);
    font-family: 'Montserrat', sans-serif;
  }
  .brand {
    position: absolute;
    top: 92px;
    left: 0;
    width: 100%;
    text-align: center;
    font-family: 'Montserrat', sans-serif;
    font-weight: 800;
    font-size: 54px;
    letter-spacing: 4px;
    color: var(--brand-grey);
    margin: 0;
    z-index: 3;
  }
  .product-photo {
    position: absolute;
    left: 600px;
    top: 300px;
    width: 360px;
    height: 690px;
    border-radius: 180px 0 0 160px;
    background: radial-gradient(ellipse at 70% 25%, var(--fruit-yellow) 0%, #e7a91b 35%, transparent 62%),
                radial-gradient(ellipse at 40% 72%, var(--gum-amber) 0%, #c77248 40%, transparent 70%);
    z-index: 1;
  }
  .title {
    position: absolute;
    left: 72px;
    top: 210px;
    width: 800px;
    height: 230px;
    z-index: 2;
  }
  .title text {
    font-family: 'Bebas Neue', sans-serif;
    font-size: 300px;
  }
  .title .title-light { fill: url(#leafGradient); }
  .title .title-dark { fill: var(--ink); }
  .subtitle {
    position: absolute;
    top: 462px;
    left: 79px;
    width: 775px;
    margin: 0;
    font-family: 'Oswald', sans-serif;
    font-weight: 400;
    font-size: 40px;
    letter-spacing: 11.5px;
    color: var(--ink);
    white-space: nowrap;
    z-index: 3;
  }
  .band-claims {
    position: absolute;
    left: 0;
    top: 610px;
    width: 680px;
    height: 198px;
    background: var(--band-black);
    z-index: 1;
  }
  .claim {
    position: absolute;
    margin: 0;
    font-family: 'Oswald', sans-serif;
    font-weight: 300;
    font-size: 34px;
    color: var(--white);
    white-space: nowrap;
  }
  .claim-sugar { left: 57px; top: 38px; }
  .claim-vegan { left: 107px; top: 120px; }
  .claim-rule {
    position: absolute;
    left: 107px;
    top: 101px;
    width: 286px;
    height: 3px;
    background: var(--rule-green);
  }
  .band-natural {
    position: absolute;
    left: 0;
    top: 808px;
    width: 720px;
    height: 68px;
    background: linear-gradient(90deg, var(--band-orange-light) 0%, var(--band-orange) 70%, rgba(180,84,31,0) 100%);
    z-index: 1;
  }
  .natural-text {
    position: absolute;
    left: 117px;
    top: 12px;
    margin: 0;
    font-family: 'Montserrat', sans-serif;
    font-weight: 400;
    font-size: 30px;
    letter-spacing: 2px;
    color: var(--white);
  }
  .band-info {
    position: absolute;
    left: 0;
    top: 876px;
    width: 100%;
    height: 194px;
    background: linear-gradient(90deg, var(--band-green-light) 0%, var(--band-green) 50%, #2f4a1c 80%, var(--band-green) 100%);
    z-index: 0;
  }
  .count {
    position: absolute;
    left: 26px;
    top: 52px;
    margin: 0;
    color: var(--white);
    white-space: nowrap;
  }
  .count-number {
    font-family: 'Oswald', sans-serif;
    font-weight: 300;
    font-size: 104px;
    line-height: 1;
  }
  .count-unit {
    font-family: 'Montserrat', sans-serif;
    font-size: 30px;
    letter-spacing: 2px;
    margin-left: 14px;
  }
  .supplement {
    position: absolute;
    right: 52px;
    top: 122px;
    margin: 0;
    font-family: 'Montserrat', sans-serif;
    font-size: 30px;
    letter-spacing: 2px;
    color: var(--white);
    z-index: 3;
  }
</style>
</head>
<body>
  <main class="label">
    <p class="brand">HALVORA</p>

    <div class="product-photo" role="img" aria-label="Pineapple wedges and pieces of amber Senegalese acacia gum"></div>

    <svg class="title" viewBox="0 0 800 230" aria-label="BrioKern">
      <defs>
        <linearGradient id="leafGradient" x1="0" y1="0" x2="1" y2="0">
          <stop offset="0" stop-color="#4e6b36"/>
          <stop offset="1" stop-color="#1f3a12"/>
        </linearGradient>
      </defs>
      <text class="title-light" x="0" y="222" textLength="380" lengthAdjust="spacingAndGlyphs">BRIO</text>
      <text class="title-dark" x="395" y="222" textLength="405" lengthAdjust="spacingAndGlyphs">KERN</text>
    </svg>

    <p class="subtitle">SENEGALESE ACACIA FIBER</p>

    <section class="band-claims">
      <p class="claim claim-sugar">NO ADDED SUGAR OR SALT</p>
      <div class="claim-rule"></div>
      <p class="claim claim-vegan">VEGAN PRODUCT</p>
    </section>

    <section class="band-natural">
      <p class="natural-text">100% NATURAL</p>
    </section>

    <section class="band-info">
      <p class="count"><span class="count-number">100</span><span class="count-unit">CAPS</span></p>
      <p class="supplement">DIETARY SUPPLEMENT</p>
    </section>
  </main>
</body>
</html>
```